Homepage for experience sharing site- interesting, fun and personable!

We need a homepage design for an experience sharing website. The tag line is 'find, promote and share great times!' The homepage should be exciting and innovative and illustrate the values of the site: possibility, freedom and life. It should be fun and personable.

To give you a clearer example, here are a few of the 'great times' users will be sharing on the site:

Club night, warehouse rave or beach gig
Antarctic expedition, Cambodian jungle trek
Cooking and surfing classes
Sumo speed dating
Drag racing and quad biking
Birthday parties, pub crawls and comedy nights

We like the idea of some sort of map or background image from which a few experiences pop up; however we are open to other ideas. The links below should give you an idea of the concept.

http://www.korvane.com/harbor#/harbor-story
http://www.pimbleo.com/map/
http://www.vidquarra.com/watch?v=QT7KWLR2zpa
Updates

Hi,

please do not feel that your design must include a map, that was just an idea. If you can produce a design that delivers the message immediately and gets the user interested without a map then that is great! 

Please do not feel constrained.

Thanks,

Marisol

Hi,

I've created and attached two examples to the brief, which I hope will provide some guidance. I want the homepage design to concentrate on the human element and the concept of creating and sharing experiences.

Thanks,

Marisol  

Target Market(s)

18-37 age range. People who enjoy life and new experiences.

Industry/Entity Type

Racing

Requirements
Must have
• It must communicate the human element of the site... please see the attached examples I made as guidance

It must deliver the message as simply as possible

Could you ensure that your design includes the following elements please:

* breadcrumbs
* a search box
* the login and register should be part of the header block
Should not have
• Unnecessary elements

Only yellow

```html
<!DOCTYPE html>
<html lang="en">
<head>
<meta charset="utf-8">
<title>GladDays.com – Find, promote and share great times</title>
<link href="https://fonts.googleapis.com/css2?family=Passion+One:wght@400&family=Quicksand:wght@500&family=Crimson+Text:ital,wght@1,600&family=Italianno&family=Gochi+Hand&family=Luckiest+Guy&family=Oswald:wght@500&family=Open+Sans:wght@400;700&display=swap" rel="stylesheet">
<style>
:root{
  --yellow:#fff200;
  --orange:#ffa800;
  --orange-deep:#f59a00;
  --cream:#f2eee3;
  --card:#f1f1ef;
  --card-edge:#d9d6cc;
  --brown:#6b4a12;
  --brown-soft:#8a6a2a;
  --tab-top:#ffd54a;
  --ink:#111;
  --label:#e9e7d4;
  --label-end:#cfcdb2;
}
*{box-sizing:border-box;margin:0;padding:0}
html,body{width:1200px;height:1126px;overflow:hidden}
body{position:relative;background:var(--cream);font-family:"Open Sans",Arial,sans-serif;color:var(--ink)}
.abs{position:absolute}

.site-header{left:0;top:0;width:1200px;height:120px;background:var(--yellow)}
.header-rule{left:0;top:120px;width:1200px;height:10px;background:var(--orange)}
.brand{left:48px;top:38px;font-family:"Passion One",sans-serif;font-size:52px;letter-spacing:1px;color:var(--ink);line-height:1}
.account{right:44px;top:38px;font-family:Arial,sans-serif;font-size:19px;color:var(--ink)}
.account span{margin:0 14px}
.main-nav{left:506px;top:79px;display:flex;gap:2px}
.nav-tab{height:41px;display:flex;align-items:center;justify-content:center;background:linear-gradient(var(--tab-top),var(--orange));font-family:"Crimson Text",serif;font-style:italic;font-weight:600;font-size:24px;color:#2a1a00;box-shadow:2px 0 2px rgba(0,0,0,.2)}

.headline{left:42px;top:172px;font-family:"Quicksand",sans-serif;font-size:35px;color:var(--brown-soft)}
.headline b{font-weight:500;font-size:44px;color:var(--orange)}

.feature-frame{left:14px;top:240px;width:459px;height:527px;background:#fff;box-shadow:0 0 10px rgba(0,0,0,.25)}
.feature-photo{left:43px;top:276px;width:394px;height:457px;background:linear-gradient(180deg,#9a9a9a 0%,#555 45%,#262626 75%,#0c0c0c 100%)}
.feature-caption{left:62px;top:672px;font-family:"Gochi Hand",cursive;font-size:34px;color:var(--orange)}
.feature-caption b{font-weight:400;font-size:42px}
.corner{width:46px;height:46px}
.details-bar{left:24px;top:775px;width:437px;height:48px;background:linear-gradient(#eef0e6,#c9ccbc);box-shadow:0 2px 4px rgba(0,0,0,.3);padding:8px 14px;font-family:Arial,sans-serif;font-size:14px}
.details-bar strong{font-family:"Oswald",sans-serif;font-weight:500;font-size:21px;margin-right:6px}

.share-label{left:716px;top:149px;width:446px;height:57px;background:linear-gradient(var(--label),var(--label-end));border-radius:6px 6px 0 0;display:flex;align-items:center;justify-content:center;font-family:"Crimson Text",serif;font-style:italic;font-weight:600;font-size:23px;color:var(--brown);box-shadow:0 2px 4px rgba(0,0,0,.2)}

.profile{background:var(--card);border:2px solid var(--card-edge);border-radius:16px;box-shadow:0 2px 6px rgba(0,0,0,.18)}
.profile .photo{position:absolute;left:10px;top:14px;right:10px;height:178px;border-radius:6px}
.profile .name{position:absolute;left:0;right:0;bottom:18px;text-align:center;font-family:"Italianno",cursive;font-size:40px;color:var(--brown)}

.more-tab{left:482px;top:543px;width:91px;height:284px}
.more-text{left:482px;top:543px;width:80px;height:284px;display:flex;align-items:center;justify-content:center}
.more-text p{transform:rotate(-90deg);white-space:nowrap;font-family:"Crimson Text",serif;font-style:italic;font-weight:600;font-size:21px;line-height:1.05;color:var(--brown);text-align:center}

.promo{top:851px;height:158px;width:379px;border:2px solid #d8d6bf;border-radius:6px;overflow:hidden}
.promo .photo{position:absolute;inset:0}
.promo-title{position:absolute;font-family:"Luckiest Guy",cursive;color:var(--yellow);-webkit-text-stroke:1.5px #3a2a00;line-height:.9}
.btn{position:absolute;background:linear-gradient(#ffe04a,var(--orange-deep));border:2px solid #6b4a00;border-radius:8px;font-family:Arial,sans-serif;font-weight:700;font-style:italic;font-size:15px;color:#111;display:flex;align-items:center;justify-content:center}
.register-title{position:absolute;font-family:"Oswald",sans-serif;font-weight:500;font-size:27px;color:#111;text-shadow:0 0 3px #fff,0 0 3px #fff}
.phone{position:absolute;font-family:"Oswald",sans-serif;font-weight:500;font-size:28px;color:#111}

.site-footer{left:0;top:1030px;width:1200px;height:90px;background:var(--orange);display:flex;align-items:center;justify-content:center;font-size:16px;color:#222;box-shadow:0 -4px 6px rgba(0,0,0,.12)}
.footer-base{left:0;top:1120px;width:1200px;height:6px;background:#cfcfcf}
</style>
</head>
<body>

<header>
  <div class="abs site-header"></div>
  <div class="abs header-rule"></div>
  <div class="abs brand">GLADDAYS.COM</div>
  <div class="abs account">Login<span>|</span>Register</div>
  <nav class="abs main-nav">
    <div class="nav-tab" style="width:201px">Find Great Times</div>
    <div class="nav-tab" style="width:239px">Promote Great Times</div>
    <div class="nav-tab" style="width:224px">Share Great Times</div>
  </nav>
</header>

<main>
  <h1 class="abs headline">Have you lived <b>TODAY!</b></h1>

  <section>
    <div class="abs feature-frame"></div>
    <div class="abs feature-photo" role="img" aria-label="Black and white photo of a woman photographing the sea from a rocky shore"></div>
    <svg class="abs corner" style="left:24px;top:250px" viewBox="0 0 46 46"><path d="M0 0H46V10H10V46H0Z" fill="#555"/></svg>
    <svg class="abs corner" style="left:417px;top:250px" viewBox="0 0 46 46"><path d="M0 0H46V46H36V10H0Z" fill="#555"/></svg>
    <svg class="abs corner" style="left:24px;top:711px" viewBox="0 0 46 46"><path d="M0 0H10V36H46V46H0Z" fill="#555"/></svg>
    <svg class="abs corner" style="left:417px;top:711px" viewBox="0 0 46 46"><path d="M36 0H46V46H0V36H36Z" fill="#555"/></svg>
    <div class="abs feature-caption">experince of the <b>DAY</b></div>
    <div class="abs details-bar"><strong>See in Details</strong>click here to share all of his experiences</div>
  </section>

  <section>
    <div class="abs share-label">Clcik on profiles to share their experiences</div>

    <div class="abs profile" style="left:549px;top:237px;width:224px;height:266px">
      <div class="photo" style="background:linear-gradient(135deg,#3a3a3a,#111 60%,#6a5040)" role="img" aria-label="Photo of a young man holding a camera"></div>
      <div class="name">Jack Smith</div>
    </div>
    <div class="abs profile" style="left:752px;top:276px;width:206px;height:269px">
      <div class="photo" style="top:14px;background:linear-gradient(160deg,#6fb0e8,#c8a080 55%,#3a7a4a)" role="img" aria-label="Photo of a group of laughing friends under a blue sky"></div>
      <div class="name">Rich Stuart</div>
    </div>
    <div class="abs profile" style="left:940px;top:228px;width:224px;height:263px">
      <div class="photo" style="background:linear-gradient(140deg,#e0b8a0,#c84a40 60%,#a02a2a)" role="img" aria-label="Photo of two young women in red"></div>
      <div class="name">Nadia Vale</div>
    </div>
    <div class="abs profile" style="left:581px;top:485px;width:224px;height:267px">
      <div class="photo" style="background:linear-gradient(140deg,#d8a860,#e8c09a 50%,#3a2a1a)" role="img" aria-label="Photo of a smiling blonde woman"></div>
      <div class="name">Loila Smith</div>
    </div>
    <div class="abs profile" style="left:740px;top:555px;width:226px;height:269px">
      <div class="photo" style="background:linear-gradient(160deg,#6a7aa8,#2a3a5a 55%,#1a2238)" role="img" aria-label="Photo of a man fishing by a lake"></div>
      <div class="name">Larry Gomes</div>
    </div>
    <div class="abs profile" style="left:916px;top:477px;width:224px;height:268px">
      <div class="photo" style="background:linear-gradient(170deg,#d8d8d8,#9a9a9a 55%,#5a5a5a)" role="img" aria-label="Black and white photo of three young men running on a beach"></div>
      <div class="name">Rowan Crest</div>
    </div>

    <svg class="abs more-tab" viewBox="0 0 91 284"><path d="M6 0H72Q80 0 80 8V118L91 140L80 162V276Q80 284 72 284H6Q0 284 0 276V8Q0 0 6 0Z" fill="#e2e0c6" stroke="#cfcdb2" stroke-width="2"/></svg>
    <div class="abs more-text"><p>Want to see more Profiles<br>Clcik Here</p></div>
  </section>

  <section>
    <div class="abs promo" style="left:24px">
      <div class="photo" style="background:linear-gradient(90deg,#b08a6a,#d8c8a8 45%,#ece4cc)" role="img" aria-label="Photo of a laughing father and children"></div>
      <div class="promo-title" style="left:150px;top:22px;font-size:33px">what's your<br>experience?</div>
      <div class="btn" style="left:207px;top:98px;width:158px;height:34px">Tell Us &amp; We Share</div>
    </div>
    <div class="abs promo" style="left:411px">
      <div class="photo" style="background:linear-gradient(110deg,#8a98a8,#e8ecef 40%,#6a4a30 75%,#3a2418)" role="img" aria-label="Photo of a man typing on a laptop"></div>
      <div class="register-title" style="left:140px;top:56px">NEW? REGISTER NOW</div>
      <div class="btn" style="left:266px;top:98px;width:100px;height:34px;font-style:normal">Register</div>
    </div>
    <div class="abs promo" style="left:798px">
      <div class="photo" style="background:linear-gradient(90deg,#c8a070,#e6d2b0 35%,#e2dcc6)" role="img" aria-label="Photo of a support agent wearing a headset"></div>
      <div class="promo-title" style="left:156px;top:70px;font-size:34px">CONTACT US</div>
      <div class="phone" style="left:166px;top:103px">888 3170 4172</div>
    </div>
  </section>
</main>

<footer>
  <div class="abs site-footer">© 2011, All Rights Reserved, www.gladdays.com</div>
  <div class="abs footer-base"></div>
</footer>

</body>
</html>
```